Tavlune

I'd like new business card design options. I'll need to provide updated contact info although after the deign is complete. We are in IT, specifically in the data backup, archiving and disaster recovery verticals.

Business

```html
<!DOCTYPE html>
<html lang="en">
<head>
<meta charset="utf-8">
<title>Tavlune Business Card</title>
<link rel="stylesheet" href="https://fonts.googleapis.com/css2?family=Jost:wght@700&family=Open+Sans:wght@400;600;700&display=swap">
<style>
  :root {
    --page-bg: #e9e7e3;
    --card-bg: #f4f2ee;
    --map-tone: #dcdad6;
    --brand-blue: #1a5fa8;
    --light-blue: #3a9ad6;
    --text-grey: #55575c;
    --rule-blue: #3d7cc4;
  }
  html, body {
    margin: 0;
    padding: 0;
    width: 1200px;
    height: 1200px;
    overflow: hidden;
    background: var(--page-bg);
  }
  .canvas {
    position: relative;
    width: 1200px;
    height: 1200px;
  }
  .card {
    position: absolute;
    left: 100px;
    top: 314px;
    width: 1000px;
    height: 572px;
    background: var(--card-bg);
    box-shadow: 0 6px 24px rgba(0,0,0,0.12);
    overflow: hidden;
    font-family: "Open Sans", sans-serif;
  }
  .world-map {
    position: absolute;
    inset: 0;
    background:
      radial-gradient(ellipse 30% 40% at 70% 30%, var(--map-tone) 0%, transparent 70%),
      radial-gradient(ellipse 22% 35% at 40% 78%, var(--map-tone) 0%, transparent 70%),
      radial-gradient(ellipse 20% 30% at 92% 60%, var(--map-tone) 0%, transparent 70%);
    opacity: 0.8;
  }
  .brand {
    position: absolute;
    left: 120px;
    top: 66px;
    display: flex;
    align-items: center;
    gap: 28px;
  }
  .brand-dot {
    width: 110px;
    height: 110px;
    border-radius: 50%;
    background: var(--light-blue);
  }
  .brand-name {
    font-family: "Open Sans", sans-serif;
    font-weight: 700;
    font-size: 70px;
    color: var(--brand-blue);
    line-height: 1;
  }
  .brand-tagline {
    font-family: "Open Sans", sans-serif;
    font-weight: 600;
    font-size: 28px;
    color: var(--light-blue);
    margin-top: 10px;
  }
  .person {
    position: absolute;
    left: 380px;
    top: 232px;
  }
  .person-name {
    font-family: "Jost", sans-serif;
    font-weight: 700;
    font-size: 64px;
    letter-spacing: 3px;
    color: var(--brand-blue);
    line-height: 1;
  }
  .person-role {
    font-size: 29px;
    color: var(--text-grey);
    margin-top: 12px;
    display: flex;
    align-items: center;
    gap: 10px;
  }
  .person-role .phone-icon {
    width: 26px;
    height: 26px;
  }
  .contact-rule {
    position: absolute;
    left: 0;
    right: 40px;
    top: 418px;
    height: 2px;
    background: var(--rule-blue);
  }
  .contact-item {
    position: absolute;
    top: 385px;
    width: 300px;
    display: flex;
    flex-direction: column;
    align-items: center;
  }
  .contact-icon {
    width: 68px;
    height: 68px;
    border-radius: 50%;
    background: var(--brand-blue);
    display: flex;
    align-items: center;
    justify-content: center;
  }
  .contact-text {
    margin-top: 12px;
    font-size: 26px;
    line-height: 1.3;
    color: var(--text-grey);
    text-align: center;
    white-space: nowrap;
  }
  .contact-address { left: 130px; }
  .contact-fax { left: 400px; }
  .contact-web { left: 680px; }
</style>
</head>
<body>
<div class="canvas">
  <div class="card">
    <div class="world-map" role="img" aria-label="Faint grey world map in the card background"></div>

    <div class="brand">
      <div class="brand-dot"></div>
      <div>
        <div class="brand-name">Tavlune</div>
        <div class="brand-tagline">Secure Backup Partners</div>
      </div>
    </div>

    <div class="person">
      <div class="person-name">JOHN DOE</div>
      <div class="person-role">
        <span>Director |</span>
        <svg class="phone-icon" viewBox="0 0 26 26" aria-hidden="true">
          <circle cx="13" cy="13" r="13" fill="var(--brand-blue)"/>
          <rect x="9" y="5" width="8" height="16" rx="1.5" fill="#fff"/>
          <rect x="10.5" y="7" width="5" height="7" fill="var(--brand-blue)"/>
        </svg>
        <span>1-234-567890</span>
      </div>
    </div>

    <div class="contact-rule"></div>

    <div class="contact-item contact-address">
      <div class="contact-icon">
        <svg width="30" height="36" viewBox="0 0 30 36" aria-hidden="true">
          <path d="M15 2C8 2 3 7 3 13.5 3 22 15 34 15 34s12-12 12-20.5C27 7 22 2 15 2z" fill="none" stroke="#fff" stroke-width="3"/>
          <circle cx="15" cy="13.5" r="4" fill="#fff"/>
        </svg>
      </div>
      <div class="contact-text">Dummy city<br>Dummy Country Land</div>
    </div>

    <div class="contact-item contact-fax">
      <div class="contact-icon">
        <svg width="36" height="32" viewBox="0 0 36 32" aria-hidden="true">
          <rect x="9" y="3" width="18" height="9" fill="#fff"/>
          <rect x="3" y="12" width="30" height="13" rx="2" fill="#fff"/>
          <rect x="9" y="20" width="18" height="9" fill="#fff" stroke="var(--brand-blue)" stroke-width="2"/>
        </svg>
      </div>
      <div class="contact-text">xxx-xxxx-xxxx<br>xxx-xxxx-xxxx</div>
    </div>

    <div class="contact-item contact-web">
      <div class="contact-icon">
        <svg width="36" height="36" viewBox="0 0 36 36" aria-hidden="true">
          <circle cx="18" cy="18" r="14" fill="none" stroke="#fff" stroke-width="3"/>
          <ellipse cx="18" cy="18" rx="6" ry="14" fill="none" stroke="#fff" stroke-width="2"/>
          <line x1="4" y1="18" x2="32" y2="18" stroke="#fff" stroke-width="2"/>
        </svg>
      </div>
      <div class="contact-text">www.tavlune.com<br>john@tavlune.com</div>
    </div>
  </div>
</div>
</body>
</html>
```